Business card for a Exhibition booth fabrication company

Hi. My company would like to change our corporate name card. We are an events and Exhibition stand builder company. We would like our corporate name card to resonate what we do. I need someone to create something unique that relates to the industry that I am in. The graphic designer should be creative to incorporate the elements of my industry and try to blend in well in the design of the card. Our aim is to ensure that we are unique and our card can look different from our competitors.
Updates

The decision maker was very busy and didnt had time to make this decision

Target Market(s)

Marketing and events manager from all companies

Contact Information for Business Card

The business card should have the following details:
Name
Job Title
Email
Website

Colors

Designer to choose colors to be used in the design.

Requirements
Must have
• The card must be look something that is relevant to the service that I am providing. My website is: www.velmora-buildworks.example
• You can see my website to get more information on what service that I am doing
Nice to have
• On the back of my card, I would like to have a globe image with the incorporation of my company logo. This is to indicate that my services can be done in any part of the world.

```html
<!DOCTYPE html>
<html lang="en">
<head>
<meta charset="utf-8">
<title>Velmora Buildworks – Business Card</title>
<link href="https://fonts.googleapis.com/css2?family=Michroma&family=Roboto:ital,wght@0,400;1,400&display=swap" rel="stylesheet">
<style>
  :root {
    --page-bg: #2a2a2c;
    --card-white: #f4f4f4;
    --card-white-shade: #e2e2e2;
    --card-dark: #1b1b1c;
    --map-tone: #2b2b2d;
    --ink: #3a3a3a;
    --ink-soft: #6b6b6b;
    --accent: #d8222a;
    --brand-text: #ececec;
    --rule: #b9b9b9;
  }
  * { margin: 0; padding: 0; box-sizing: border-box; }
  html, body { width: 1200px; height: 900px; overflow: hidden; }
  body {
    background: var(--page-bg);
    display: flex;
    flex-direction: column;
    align-items: center;
    justify-content: center;
    gap: 56px;
  }
  .card {
    width: 600px;
    height: 343px;
    border-radius: 3px;
    position: relative;
    overflow: hidden;
    box-shadow: 0 14px 30px rgba(0,0,0,.45);
  }

  /* Front */
  .card-front {
    background: linear-gradient(160deg, var(--card-white) 0%, #ffffff 45%, var(--card-white-shade) 100%);
    display: flex;
    align-items: center;
    justify-content: center;
    gap: 24px;
  }
  .identity { text-align: right; }
  .identity__name {
    font-family: "Michroma", sans-serif;
    font-size: 19px;
    letter-spacing: 1.5px;
    color: var(--ink);
  }
  .identity__title {
    font-family: "Roboto", sans-serif;
    font-style: italic;
    font-size: 13px;
    color: var(--ink-soft);
    margin-top: 4px;
  }
  .divider {
    width: 1px;
    height: 64px;
    background: var(--rule);
    transform: translateY(22px);
  }
  .contact-list {
    list-style: none;
    font-family: "Roboto", sans-serif;
    font-size: 12px;
    color: var(--ink-soft);
    transform: translateY(28px);
  }
  .contact-list li {
    display: flex;
    align-items: center;
    gap: 7px;
    line-height: 18px;
  }
  .contact-list svg { width: 10px; height: 10px; flex: none; }

  /* Back */
  .card-back { background: var(--card-dark); }
  .world-map {
    position: absolute;
    inset: 20px 30px;
    border-radius: 40%;
    background: radial-gradient(ellipse at center, var(--map-tone) 0%, var(--map-tone) 45%, rgba(43,43,45,0) 75%);
  }
  .brand {
    position: absolute;
    inset: 0;
    display: flex;
    align-items: center;
    justify-content: center;
    gap: 14px;
  }
  .brand__dot {
    width: 18px;
    height: 18px;
    border-radius: 50%;
    background: var(--accent);
  }
  .brand__name {
    font-family: "Michroma", sans-serif;
    font-size: 22px;
    letter-spacing: 2px;
    color: var(--brand-text);
  }
</style>
</head>
<body>

  <section class="card card-front" aria-label="Business card front">
    <div class="identity">
      <p class="identity__name">ADRIAN COLE</p>
      <p class="identity__title">Managing Director</p>
    </div>
    <div class="divider"></div>
    <ul class="contact-list">
      <li>
        <svg viewBox="0 0 10 10" aria-hidden="true"><path d="M2 1 L4 1 L4.6 3.2 L3.4 4 Q4.4 6 6 6.6 L6.8 5.4 L9 6 L9 8 Q9 9 8 9 Q1 8.4 1 2 Q1 1 2 1Z" fill="var(--accent)"/></svg>
        +65 90004417
      </li>
      <li>
        <svg viewBox="0 0 10 10" aria-hidden="true"><rect x="0.5" y="2" width="9" height="6.5" fill="var(--accent)"/><path d="M0.5 2 L5 5.6 L9.5 2" fill="none" stroke="#fff" stroke-width="0.9"/></svg>
        info@velmora-buildworks.example
      </li>
      <li>
        <svg viewBox="0 0 10 10" aria-hidden="true"><g fill="none" stroke="var(--accent)" stroke-width="0.9"><circle cx="5" cy="5" r="4.2"/><ellipse cx="5" cy="5" rx="1.8" ry="4.2"/><path d="M0.8 5 H9.2 M1.6 2.8 H8.4 M1.6 7.2 H8.4"/></g></svg>
        www.velmora-buildworks.example
      </li>
    </ul>
  </section>

  <section class="card card-back" aria-label="Business card back">
    <div class="world-map" role="img" aria-label="Faint world map spanning the card"></div>
    <div class="brand">
      <span class="brand__dot"></span>
      <span class="brand__name">VELMORA BUILDWORKS</span>
    </div>
  </section>

</body>
</html>
```